Jackpot Display Wallpaper Design

We develop Jackpot Systems for Casinos and have a web based Jackpot Odometer display. Our software works by superimposing dynamic content over a fixed background.

We require the design of a fixed background of dimensions 1920 x 1080 incorporating higher quality graphical design work and creative ideas.

See File 4 below - "High Hand TEMPLATE". The finished work will resemble this image, with the grey background replaced with your creative design. The black panels will be replaced with your panels, with nice borders and interior shading or pattern. Our software will dynamically superimpose content over the panels. The panels should be of similar size and location to those shown although this is not strictly rigid and you can relocate or resize panels to a limited extent.

The end result when our software runs is something like File 5 below - "High Hand SAMPLE RESULT". Note that the example shows a patterned blue background, a red logo area, and grey shading within the panels.

The text within the panels is rendered dynamically by our application.

** This is a very plain design and only intended to illustrate how we superimpose text and playing cards onto a background. Do not take any design cues from this image.

Please provide the background, and blank panels. The panels can (and should) have some texture or shading that will look good when we render text over them.

Feel free to suggest a font and/or text color that you think would look good against your background and we can render the content in the font / color you suggest.

Target Market(s)

Poker Room facilities and Casinos

Industry/Entity Type

Software

Font styles to use
Sans Serif

Requirements
Must have
• - A graphic design based on the template called High Hand TEMPLATE.
• - 1920 x 1080 Photoshop image using separate layers.
• - The design needs to be edgy and reflect gaming, casinos and poker rooms.
Nice to have
• -Please see files 1, 2, and 3 below by way of "edgy" style guide.
• - For files 1, 2, 3 - ignore the "Bad Beat" wording but focus on the design style by way of example.
• - The background may or may not include the words "Poker" and / or "Jackpot"
• - You can fill in the panels with some sample content to illustrate how it will look.
• - The area at bottom containing scrolling text may be a frame with a border or just an area where we superimpose the scrolling text.

```html
<!DOCTYPE html>
<html lang="en">
<head>
<meta charset="utf-8">
<title>High Hand Bonus Display</title>
<link href="https://fonts.googleapis.com/css2?family=Montserrat:wght@500;600;700;800&display=swap" rel="stylesheet">
<style>
  :root {
    --page: #ffffff;
    --fire-deep: #c8200a;
    --fire-mid: #f0560c;
    --fire-bright: #ffb21e;
    --red-top: #e0202a;
    --red-bottom: #8a0a12;
    --panel-black: #0c0c0c;
    --panel-grey: #3a3a3a;
    --chrome-light: #f4f4f4;
    --chrome-dark: #8c8c8c;
    --text-white: #ffffff;
    --suit-red: #e0121c;
    --suit-black: #111111;
  }
  * { box-sizing: border-box; margin: 0; padding: 0; }
  html, body { width: 1200px; height: 1000px; overflow: hidden; background: var(--page); }
  body { position: relative; font-family: "Montserrat", sans-serif; }

  .display {
    position: absolute; left: 301px; top: 332px; width: 598px; height: 337px; overflow: hidden;
  }
  .display__backdrop {
    position: absolute; inset: 0;
    background:
      radial-gradient(ellipse 45% 30% at 62% 45%, rgba(255,214,80,.85), rgba(255,160,30,0) 70%),
      radial-gradient(ellipse 60% 45% at 30% 70%, rgba(255,180,40,.6), rgba(255,140,20,0) 70%),
      linear-gradient(160deg, var(--fire-deep) 0%, var(--fire-mid) 45%, var(--fire-bright) 60%, var(--fire-mid) 75%, var(--fire-deep) 100%);
  }

  .panel {
    position: absolute; top: 135px; height: 89px;
    border-radius: 6px; padding: 3px;
    background: linear-gradient(180deg, var(--chrome-light), var(--chrome-dark) 50%, var(--chrome-light));
    box-shadow: 0 2px 8px rgba(0,0,0,.45);
  }
  .panel__inner {
    height: 100%; border-radius: 4px; overflow: hidden;
    background: linear-gradient(180deg, var(--panel-grey) 0%, var(--panel-black) 30%, var(--panel-black) 75%, var(--panel-grey) 100%);
    display: flex; flex-direction: column; align-items: center; color: var(--text-white);
  }
  .panel__label {
    width: 100%; text-align: center; font-size: 9.5px; font-weight: 700; letter-spacing: .3px;
    padding: 11px 0 6px;
    background: linear-gradient(180deg, #555 0%, #1a1a1a 100%);
  }
  .panel__value { font-size: 28px; font-weight: 700; line-height: 1; margin-top: 10px; }

  .panel--prize { left: 67px; width: 107px; }
  .panel--countdown { left: 428px; width: 107px; }

  .panel--hand { left: 170px; width: 262px; top: 133px; height: 91px; z-index: 2; }
  .hand__cards { display: flex; gap: 10px; justify-content: center; padding-top: 9px; }
  .card {
    position: relative; width: 38px; height: 52px; border-radius: 3px;
    background: linear-gradient(180deg, #ffffff, #e6e6e6);
    border: 1px solid #bdbdbd;
  }
  .card__rank { position: absolute; left: 3px; top: 1px; font-size: 9px; font-weight: 700; line-height: 1; }
  .card__pip { position: absolute; left: 50%; top: 56%; transform: translate(-50%, -50%); font-size: 22px; line-height: 1; }
  .card--red { color: var(--suit-red); }
  .card--black { color: var(--suit-black); }
  .hand__caption {
    margin-top: 6px; width: 94%; text-align: center; font-size: 6.5px; font-weight: 600;
    padding: 2px 0; border-top: 1px solid #555; border-bottom: 1px solid #555;
  }

  .title-tab {
    position: absolute; left: 169px; top: 106px; width: 264px; height: 34px; z-index: 3;
    border-radius: 6px 6px 0 0; padding: 3px 3px 0;
    background: linear-gradient(180deg, var(--chrome-light), var(--chrome-dark));
  }
  .title-tab__inner {
    height: 100%; border-radius: 4px 4px 0 0;
    background: linear-gradient(180deg, var(--red-top), var(--red-bottom));
    color: var(--text-white); font-size: 17px; font-weight: 700; text-align: center; line-height: 29px; letter-spacing: .2px;
  }
</style>
</head>
<body>
  <main class="display">
    <div class="display__backdrop" role="img" aria-label="Glowing orange and red fiery backdrop with swirling golden light sparkles"></div>

    <section class="panel panel--prize">
      <div class="panel__inner">
        <div class="panel__label">PRIZE</div>
        <div class="panel__value">$250</div>
      </div>
    </section>

    <header class="title-tab"><div class="title-tab__inner">HIGH HAND BONUS</div></header>

    <section class="panel panel--hand">
      <div class="panel__inner">
        <div class="hand__cards" style="padding-top:12px">
          <div class="card card--red"><span class="card__rank">7<br>♥</span><span class="card__pip">♥</span></div>
          <div class="card card--black"><span class="card__rank">7<br>♠</span><span class="card__pip">♠</span></div>
          <div class="card card--black"><span class="card__rank">5<br>♠</span><span class="card__pip">♠</span></div>
          <div class="card card--red"><span class="card__rank">5<br>♦</span><span class="card__pip">♦</span></div>
          <div class="card card--red"><span class="card__rank">T<br>♦</span><span class="card__pip">♦</span></div>
        </div>
        <div class="hand__caption">TWO PAIR - TABLE 18 (SAM RIVERA)</div>
      </div>
    </section>

    <section class="panel panel--countdown">
      <div class="panel__inner">
        <div class="panel__label">COUNTDOWN</div>
        <div class="panel__value">1:59</div>
      </div>
    </section>
  </main>
</body>
</html>
```